UPDATE: Web Page: Meridew Public Relations

i DON'T NEED PICTURES, JUST SOMETHING CLEAN LIKE THE ARTWORK ATTACHED OR BUILT ON BUSINESS CARDS...PLEASE DESIGN AROUND THAT.

I need a clean webpage for new public relations firm that I will launch on March 1st. I HAVE JUST ADDED BUSINESS CARD MODELS FOR WEB PAGE COVER AND START IN TERMS OF DESIGN.

Pull down categories: (built on this model: http://www.quornsvalepr.com/contact/)

-Home
-Services
-Expertise
-About Us
-Press
-Contact

Garth Pelliam, CEO
Meridew Public Relations
2875 West Hallowmere Blvd.
Los Angeles CA 90047
(o) 213.555.0148
(f) 213.555.0193
garth@meridewmpr.com

Target Market(s)

Varnholt Civic Assembly, Orvane Civic Hall
Lobbying type services to government/public affairs

Industry/Entity Type

Business

Number of Pages Required

4 page

Requirements
Must have
• Portray a beautiful picture of LA City or a government hall way (not domes)
• 1. Public Relations---Pic of Advocacy
• 2. Public Affairs--pick of government capitol Sacramento/Orvane Civic Hall
• 3. Strategy & Advisory Services--Something smart like chalk board.
Nice to have
• Great Pics on slider pages
Should not have
• Varnholt Assembly Dome
• Orvane Civic Hall

```html
<!DOCTYPE html>
<html lang="en">
<head>
<meta charset="utf-8">
<title>Meridew Public Relations</title>
<link href="https://fonts.googleapis.com/css2?family=Mulish:wght@400;600;700&display=swap" rel="stylesheet">
<style>
:root{
  --ink:#262626;
  --ink-soft:#3a3a3a;
  --text:#333333;
  --muted:#6d6d6d;
  --accent:#27a9d6;
  --brand:#1f6fb4;
  --panel:#f1f1f1;
  --panel-line:#c9c9c9;
  --white:#ffffff;
  --rule:#dcdcdc;
}
*{box-sizing:border-box;margin:0;padding:0}
html,body{width:710px;height:1200px;overflow:hidden;background:var(--white)}
body{font-family:"Mulish",Arial,sans-serif;color:var(--text)}
.page{position:relative;width:710px;height:1200px;overflow:hidden}
.abs{position:absolute}

/* header */
.site-header{left:0;top:0;width:710px;height:56px;background:var(--ink)}
.brand{left:44px;top:14px;display:flex;align-items:center;gap:7px}
.brand-mark{width:26px;height:26px;border-radius:50%;background:var(--brand)}
.brand-name{font-size:17px;font-weight:700;color:var(--brand);letter-spacing:.2px}
.main-nav{left:330px;top:0;height:56px;display:flex}
.main-nav a{display:flex;align-items:center;height:56px;color:#e6e6e6;font-size:7.5px;text-decoration:none;padding:0 15px}
.main-nav a.is-active{background:var(--accent);color:var(--white);padding:0 16px}

/* hero */
.hero{left:0;top:56px;width:710px;height:266px;background:linear-gradient(180deg,#e9edf0 0%,#f6f7f8 45%,#dcdfe2 100%)}
.hero-people{left:80px;top:80px;width:570px;height:212px;background:linear-gradient(180deg,#b9b3ab 0%,#5a5c62 45%,#2f3136 100%);opacity:.55;border-radius:40px 40px 0 0}
.hero-dots{left:333px;top:267px;display:flex;gap:5px}
.hero-dots span{width:8px;height:8px;border-radius:50%;background:#111}
.hero-dots span.is-current{background:var(--accent)}

.band{left:44px;width:622px}

/* service cards */
.service-card{top:312px;width:177px;height:196px;background:var(--panel);border:1px solid var(--panel-line);text-align:center}
.service-title{margin-top:13px;font-size:12.5px;font-weight:600;color:var(--accent)}
.service-icon{display:block;margin:9px auto 0;width:58px;height:58px}
.service-text{margin:11px auto 0;width:152px;font-size:7.3px;line-height:12.6px;color:var(--text)}
.btn-dark{top:494px;width:78px;height:24px;background:var(--ink);color:var(--white);font-size:7.3px;display:flex;align-items:center;justify-content:center;letter-spacing:.3px}

/* welcome */
.welcome-shade{left:0;top:548px;width:710px;height:10px;background:linear-gradient(180deg,#f0f0f0,#fff)}
.welcome-title{left:0;top:570px;width:710px;text-align:center;font-size:16px;font-weight:600;color:var(--ink)}
.welcome-text{left:44px;top:599px;width:622px;text-align:center;font-size:6.6px;line-height:12.7px;color:var(--muted)}
.btn-accent{left:316px;top:656px;width:78px;height:24px;background:var(--accent);color:var(--white);font-size:7.8px;display:flex;align-items:center;justify-content:center;letter-spacing:.3px}
.rule{left:44px;top:702px;width:622px;height:1px;background:var(--rule)}

/* industries */
.section-title{font-size:15px;font-weight:600;color:var(--ink)}
.industries-title{left:44px;top:720px}
.carousel-arrows{left:480px;top:727px;display:flex;gap:8px}
.industry{top:750px;width:143px}
.industry-photo{width:143px;height:84px}
.industry-name{margin-top:9px;font-size:9.8px;font-weight:600;color:var(--accent)}
.industry-text{margin-top:4px;font-size:6.6px;line-height:11px;color:var(--text)}

/* news */
.news{left:523px;top:722px;width:142px;height:179px;background:var(--panel);border:1px solid var(--panel-line);padding:0 10px}
.news-title{margin-top:9px;font-size:15px;font-weight:600;color:var(--ink)}
.news-item{padding:5px 0 7px;border-bottom:1px solid var(--rule)}
.news-item:last-child{border-bottom:0}
.news-item:first-of-type{padding-top:3px}
.news-date{font-size:6.6px;color:var(--accent)}
.news-text{margin-top:2px;font-size:6.6px;line-height:11px;color:var(--text)}

/* founder & contact */
.panel-title{top:948px;font-size:15px;font-weight:600;color:var(--white)}
.founder-video{left:62px;top:978px;width:229px;height:136px;border:2px solid #cfcfcf;background:linear-gradient(135deg,#d9dde0 0%,#a6aab0 50%,#3c4350 100%)}
.play-button{left:159px;top:1028px}
.contact-box{left:310px;top:978px;width:341px;height:136px;background:var(--panel);border:2px solid #cfcfcf}
.field{background:var(--white);border:1px solid #bdbdbd;font-size:7px;color:#8a8a8a;padding:0 7px;display:flex;align-items:center}
.field-message{align-items:flex-start;padding-top:6px}
.btn-submit{left:562px;top:1083px;width:64px;height:19px;background:var(--accent);color:var(--white);font-size:7.3px;display:flex;align-items:center;justify-content:center;letter-spacing:.3px}

/* footer */
.site-footer{left:0;top:1130px;width:710px;height:70px;background:var(--ink)}
.footer-nav{left:44px;top:1148px;display:flex;gap:0}
.footer-nav a{color:#e6e6e6;font-size:7.5px;text-decoration:none;margin-right:31px}
.copyright{left:44px;top:1172px;font-size:6.6px;color:#8d8d8d}
.social{left:555px;top:1157px;display:flex;gap:3px}
.social span{width:17px;height:17px;border-radius:50%;background:var(--white)}
</style>
</head>
<body>
<div class="page">

  <header class="abs site-header">
    <div class="abs brand"><span class="brand-mark"></span><span class="brand-name">Meridew Public Relations</span></div>
    <nav class="abs main-nav">
      <a class="is-active" href="#">Home</a>
      <a href="#">Services</a>
      <a href="#">Expertise</a>
      <a href="#">About Us</a>
      <a href="#">Press</a>
      <a href="#">Contact</a>
    </nav>
  </header>

  <section class="abs hero" role="img" aria-label="Slider photo: a team of six business people standing in a bright glass office"></section>
  <div class="abs hero-people" aria-hidden="true"></div>
  <div class="abs hero-dots"><span class="is-current"></span><span></span><span></span><span></span></div>

  <svg class="abs band" style="top:274px" width="622" height="164" viewBox="0 0 622 164" aria-hidden="true">
    <path d="M0 2 Q311 32 622 2 L622 164 L0 164 Z" fill="#262626"/>
  </svg>

  <article class="abs service-card" style="left:62px">
    <h2 class="service-title">Public Relations</h2>
    <svg class="service-icon" viewBox="0 0 58 58" aria-hidden="true">
      <circle cx="29" cy="29" r="29" fill="#27a9d6"/>
      <path d="M12 27 L20 21 L29 26 L38 21 L46 27 L38 36 L29 31 L20 36 Z" fill="none" stroke="#fff" stroke-width="2.6" stroke-linejoin="round"/>
      <path d="M24 29 L32 35" stroke="#fff" stroke-width="2.4" stroke-linecap="round"/>
    </svg>
    <p class="service-text">Lorem ipsum dolor sit amet, consect- etuer adipiscing elit, sed diam nonummy nibh euismod tincidunt ut laoreet dolore magna aliquam erat volutpat</p>
  </article>
  <div class="abs btn-dark" style="left:112px">READ MORE</div>

  <article class="abs service-card" style="left:266px">
    <h2 class="service-title">Marketing</h2>
    <svg class="service-icon" viewBox="0 0 58 58" aria-hidden="true">
      <circle cx="29" cy="29" r="29" fill="#27a9d6"/>
      <path d="M15 26 L15 34 L21 34 L38 42 L38 18 L21 26 Z" fill="#fff"/>
      <path d="M18 34 L21 42 L25 42 L23 34 Z" fill="#fff"/>
      <path d="M42 25 Q45 30 42 35" fill="none" stroke="#fff" stroke-width="2" stroke-linecap="round"/>
    </svg>
    <p class="service-text">Lorem ipsum dolor sit amet, consect- etuer adipiscing elit, sed diam nonummy nibh euismod tincidunt ut laoreet dolore magna aliquam erat volutpat</p>
  </article>
  <div class="abs btn-dark" style="left:316px">READ MORE</div>

  <article class="abs service-card" style="left:470px">
    <h2 class="service-title">Social Media</h2>
    <svg class="service-icon" viewBox="0 0 58 58" aria-hidden="true">
      <circle cx="29" cy="29" r="29" fill="#27a9d6"/>
      <path d="M14 18 H44 V36 H27 L20 43 V36 H14 Z" fill="#fff"/>
      <circle cx="22" cy="27" r="2.3" fill="#27a9d6"/>
      <circle cx="29" cy="27" r="2.3" fill="#27a9d6"/>
      <circle cx="36" cy="27" r="2.3" fill="#27a9d6"/>
    </svg>
    <p class="service-text">Lorem ipsum dolor sit amet, consect- etuer adipiscing elit, sed diam nonummy nibh euismod tincidunt ut laoreet dolore magna aliquam erat volutpat</p>
  </article>
  <div class="abs btn-dark" style="left:519px">READ MORE</div>

  <div class="abs welcome-shade" aria-hidden="true"></div>
  <h1 class="abs welcome-title">Welcome to Our Website</h1>
  <p class="abs welcome-text">Aliquam molestie, mi et imperdiet euismod, dui purus auctor tellus, et interdum lacus lectus et ante. Sed accumsan sollicitudin sapien, sit amet adipiscing turpis gravida ac. In congue, neque ac lobortis volutpat, libero mauris varius mi, vitae suscipit ipsum ligula vitae risus. Duis aliquam nibh a dui iaculis viverra id a velit. Vivamus egestas risus in magna varius commodo. Sed semper viverra egestas. Etiam pretium porttitor lectus, vel ornare neque porta volutpat.</p>
  <div class="abs btn-accent">READ MORE</div>
  <div class="abs rule"></div>

  <h2 class="abs section-title industries-title">Industries We Love</h2>
  <svg class="abs carousel-arrows" width="30" height="12" viewBox="0 0 30 12" aria-hidden="true">
    <path d="M7 1 L2 6 L7 11" fill="none" stroke="#888" stroke-width="1.3"/>
    <path d="M23 1 L28 6 L23 11" fill="none" stroke="#888" stroke-width="1.3"/>
  </svg>

  <article class="abs industry" style="left:44px">
    <div class="industry-photo" role="img" aria-label="Photo: two women shopping for beauty products" style="background:linear-gradient(135deg,#d8c7b4 0%,#b79a86 50%,#6e8c9a 100%)"></div>
    <h3 class="industry-name">Health &amp; Beauty</h3>
    <p class="industry-text">Lorem ipsum dolor sit amet, consect- etuer adipiscing elit, sed diam nonummy nibh euismod tincidunt..</p>
  </article>
  <article class="abs industry" style="left:204px">
    <div class="industry-photo" role="img" aria-label="Photo: drum kit on a concert stage under warm lights" style="background:linear-gradient(180deg,#3a3f7a 0%,#a0522d 55%,#2b1a12 100%)"></div>
    <h3 class="industry-name">Entertainment</h3>
    <p class="industry-text">Lorem ipsum dolor sit amet, consect- etuer adipiscing elit, sed diam nonummy nibh euismod tincidunt..</p>
  </article>
  <article class="abs industry" style="left:364px">
    <div class="industry-photo" role="img" aria-label="Photo: hand holding a glowing globe of technology devices" style="background:linear-gradient(135deg,#e8eef4 0%,#6fa0c8 50%,#1d3d66 100%)"></div>
    <h3 class="industry-name">Technology</h3>
    <p class="industry-text">Lorem ipsum dolor sit amet, consect- etuer adipiscing elit, sed diam nonummy nibh euismod tincidunt..</p>
  </article>

  <aside class="abs news">
    <h2 class="news-title">Latest News</h2>
    <div class="news-item"><p class="news-date">Feb 22, 2015</p><p class="news-text">Lorem ipsum dolor sit amet, consect etuer adipiscing elit, sed diam</p></div>
    <div class="news-item"><p class="news-date">Feb 22, 2015</p><p class="news-text">Lorem ipsum dolor sit amet, consect etuer adipiscing elit, sed diam</p></div>
    <div class="news-item"><p class="news-date">Feb 22, 2015</p><p class="news-text">Lorem ipsum dolor sit amet, consect etuer adipiscing elit, sed diam</p></div>
  </aside>

  <svg class="abs band" style="top:911px" width="622" height="166" viewBox="0 0 622 166" aria-hidden="true">
    <path d="M0 3 Q311 34 622 3" fill="none" stroke="#d6d6d6" stroke-width="2"/>
    <path d="M0 5 Q311 36 622 5 L622 166 L0 166 Z" fill="#262626"/>
  </svg>

  <h2 class="abs panel-title" style="left:61px">Meet The Founder</h2>
  <h2 class="abs panel-title" style="left:309px">Quick Contact</h2>

  <div class="abs founder-video" role="img" aria-label="Video still: the founder in a suit in a bright office"></div>
  <svg class="abs play-button" width="34" height="34" viewBox="0 0 34 34" aria-hidden="true">
    <circle cx="17" cy="17" r="15.5" fill="rgba(0,0,0,.25)" stroke="#fff" stroke-width="2"/>
    <path d="M13 10 L24 17 L13 24 Z" fill="#fff"/>
  </svg>

  <form class="abs contact-box" aria-label="Quick contact">
    <div class="abs field" style="left:14px;top:14px;width:145px;height:23px">Full Name</div>
    <div class="abs field" style="left:14px;top:43px;width:145px;height:22px">Email Address</div>
    <div class="abs field" style="left:14px;top:72px;width:145px;height:22px">Contact No.</div>
    <div class="abs field field-message" style="left:169px;top:14px;width:145px;height:80px">Enter Message</div>
  </form>
  <div class="abs btn-submit">SUBMIT</div>

  <footer class="abs site-footer"></footer>
  <nav class="abs footer-nav">
    <a href="#">Home</a><a href="#">Services</a><a href="#">Expertise</a><a href="#">About Us</a><a href="#">Press</a><a href="#">Contact</a>
  </nav>
  <p class="abs copyright">Copyright © 2015.Company Name.All Right Reserved</p>
  <div class="abs social" aria-label="Social links"><span></span><span></span><span></span><span></span><span></span></div>

</div>
</body>
</html>
```